Clean Landing Page - Design and Code

Need to create a similar landing page to example i have supplied. Need versions for Desktop, tablet and mobile. Letting the design chose color scheme based on description.

We want it to seem fresh, clean and cool.

We are basing it off this example http://torvanmesk.com/

Target Market(s)

young ambitious entreprerial women

Coding

Coded - Design and coding required

Number of Pages Required

3 page

Font styles to use
Sans Serif

Requirements
Must have
• Must be designed for responsive functionality.

```html
<!DOCTYPE html>
<html lang="en">
<head>
<meta charset="utf-8">
<title>Creator Academy – Landing Page</title>
<link rel="stylesheet" href="https://fonts.googleapis.com/css2?family=Montserrat:wght@400;500;700&family=Open+Sans:wght@400&display=swap">
<style>
  :root {
    --orange: #fb8c00;
    --orange-dark: #ec8507;
    --ink: #222222;
    --ink-soft: #333333;
    --grey-text: #6b6b6b;
    --grey-line: #c9c9c9;
    --pink: #f29bb0;
    --white: #ffffff;
  }
  * { margin: 0; padding: 0; box-sizing: border-box; }
  html, body { width: 980px; height: 1200px; overflow: hidden; background: var(--white); }
  body { font-family: "Montserrat", sans-serif; color: var(--ink); position: relative; }

  .hero {
    position: absolute; left: 0; top: 0; width: 980px; height: 512px;
    background: linear-gradient(135deg, #f6f6f6 0%, #ececec 45%, #f4f4f4 70%, #e6e6e6 100%);
    border-bottom: 1px solid #dcdcdc;
  }
  .hero-portrait {
    position: absolute; left: 504px; top: 32px; width: 320px; height: 480px;
    border-radius: 150px 150px 0 0;
    background: linear-gradient(180deg, #3a2a22 0%, #4a362c 30%, #e9e4e0 55%, #f5f2ef 85%, #d9c2b2 100%);
  }
  .brand-name {
    position: absolute; left: 99px; top: 82px;
    font-size: 30px; font-weight: 500; color: var(--orange); letter-spacing: 0.5px;
  }
  .brand-tagline {
    position: absolute; left: 104px; top: 122px;
    font-size: 17.5px; font-weight: 500; color: var(--ink); letter-spacing: 0.3px;
  }
  .brand-rule {
    position: absolute; left: 104px; top: 164px; width: 165px; height: 1px; background: #bdbdbd;
  }
  .hero-title {
    position: absolute; left: 104px; top: 204px; width: 400px;
    font-size: 33px; font-weight: 400; line-height: 42px; color: var(--ink-soft);
  }
  .hero-title strong { font-weight: 700; }
  .btn-primary {
    position: absolute; left: 102px; top: 352px; width: 367px; height: 51px;
    border-radius: 26px; background: var(--orange); color: var(--white);
    font-size: 17.5px; font-weight: 500; display: flex; align-items: center; justify-content: center;
    text-decoration: none;
  }

  .features-kicker {
    position: absolute; left: 0; width: 980px; top: 543px; text-align: center;
    font-size: 19px; color: var(--orange);
  }
  .features-title {
    position: absolute; left: 0; width: 980px; top: 566px; text-align: center;
    font-size: 24px; font-weight: 400; color: var(--ink);
  }
  .features-rule {
    position: absolute; left: 439px; top: 608px; width: 69px; height: 1px; background: var(--pink);
  }
  .feature { position: absolute; top: 656px; width: 170px; text-align: center; }
  .feature svg { display: block; margin: 0 auto; }
  .feature-text {
    margin: 10px auto 0; width: 150px; font-family: "Open Sans", sans-serif;
    font-size: 13px; line-height: 20px; color: var(--grey-text);
  }

  .cta-wave { position: absolute; left: 0; top: 860px; }
  .cta-band {
    position: absolute; left: 0; top: 920px; width: 980px; height: 218px; background: var(--orange);
  }
  .cta-title {
    position: absolute; left: 0; width: 980px; top: 966px; text-align: center;
    font-size: 32px; font-weight: 400; color: var(--white);
  }
  .btn-outline {
    position: absolute; left: 382px; top: 1026px; width: 188px; height: 42px;
    border: 1.5px solid var(--white); border-radius: 21px; color: var(--white);
    font-size: 14.5px; font-weight: 500; display: flex; align-items: center; justify-content: center;
    text-decoration: none;
  }

  .site-footer {
    position: absolute; left: 0; top: 1138px; width: 980px; height: 62px; background: var(--orange-dark);
    font-family: "Open Sans", sans-serif; font-size: 13.5px; color: var(--white);
  }
  .site-footer span, .site-footer a { position: absolute; top: 21px; color: var(--white); text-decoration: none; }
</style>
</head>
<body>

<header class="hero">
  <div class="hero-portrait" role="img" aria-label="Portrait photo of a smiling young woman with long dark hair in a white lace top"></div>
  <div class="brand-name">MARA VELIN</div>
  <div class="brand-tagline">CREATOR ACADEMY</div>
  <div class="brand-rule"></div>
  <h1 class="hero-title">The Advanced Guide to <strong>Becoming</strong> a Paid Social Media Influencer</h1>
  <a class="btn-primary" href="#">Yes, I Want Mara to Show me How</a>
</header>

<section class="features">
  <div class="features-kicker">Here is</div>
  <h2 class="features-title">What I’m Going to Show You</h2>
  <div class="features-rule"></div>

  <div class="feature" style="left:86px">
    <svg width="84" height="106" viewBox="-1 -4 84 106" fill="none">
      <path d="M41 100 L11 64 A40 40 0 1 1 71 64 Z" stroke="#d2d2d2" stroke-width="1.3" fill="#fff"/>
      <g stroke="#fb8c00" stroke-width="1.6">
        <rect x="23" y="48" width="6" height="10"/><rect x="32" y="43" width="6" height="15"/>
        <rect x="41" y="38" width="6" height="20"/><rect x="50" y="33" width="6" height="25"/>
        <path d="M23 40 L38 32 L44 34 L57 24 M51 24 H57 V30"/>
      </g>
    </svg>
    <p class="feature-text">The Little-Known Secrets to Grow a Highly Engaged Following</p>
  </div>

  <div class="feature" style="left:296px">
    <svg width="84" height="106" viewBox="-1 -4 84 106" fill="none">
      <path d="M41 100 L11 64 A40 40 0 1 1 71 64 Z" stroke="#d2d2d2" stroke-width="1.3" fill="#fff"/>
      <g stroke="#fb8c00" stroke-width="1.6">
        <rect x="22" y="28" width="38" height="28" rx="2"/><rect x="27" y="32" width="28" height="19"/>
        <path d="M36 60 H46"/><circle cx="41" cy="41.5" r="3"/>
        <path d="M44 41.5 V43 a2 2 0 0 0 3 -1 a6 6 0 1 0 -3 5"/>
      </g>
    </svg>
    <p class="feature-text">How to properly contact brands via DM and Email</p>
  </div>

  <div class="feature" style="left:497px">
    <svg width="84" height="106" viewBox="-1 -4 84 106" fill="none">
      <path d="M41 100 L11 64 A40 40 0 1 1 71 64 Z" stroke="#d2d2d2" stroke-width="1.3" fill="#fff"/>
      <g stroke="#fb8c00" stroke-width="1.6">
        <path d="M22 28 H52 V46 H32 L26 52 V46 H22 Z"/>
        <path d="M55 36 H61 V54 H57 V59 L52 54 H36 V49"/>
        <circle cx="30" cy="37" r="2"/><circle cx="37" cy="37" r="2"/><circle cx="44" cy="37" r="2"/>
      </g>
    </svg>
    <p class="feature-text">How to Negotiate your price per post.</p>
  </div>

  <div class="feature" style="left:699px">
    <svg width="84" height="106" viewBox="-1 -4 84 106" fill="none">
      <path d="M41 100 L11 64 A40 40 0 1 1 71 64 Z" stroke="#d2d2d2" stroke-width="1.3" fill="#fff"/>
      <g stroke="#fb8c00" stroke-width="1.6">
        <path d="M27 34 V46 A14 14 0 0 0 55 46 V34 H49 V46 A8 8 0 0 1 33 46 V34 Z"/>
        <path d="M27 39 H33 M49 39 H55"/>
        <path d="M42 24 L38 31 H43 L39 37"/>
      </g>
    </svg>
    <p class="feature-text">How to Attract Brands to your Feed</p>
  </div>
</section>

<svg class="cta-wave" width="980" height="70" viewBox="0 0 980 70" fill="none">
  <path d="M0 46 C80 46 140 26 206 26 C252 26 298 60 344 60 C390 60 437 24 483 24 C530 24 577 60 624 60 C671 60 718 28 765 28 C836 28 900 48 980 48 V70 H0 Z" fill="#fb8c00"/>
  <path d="M0 32 C80 32 140 14 206 14 C252 14 298 50 344 50 C390 50 437 12 483 12 C530 12 577 50 624 50 C671 50 718 16 765 16 C836 16 900 36 980 36" stroke="#c9c9c9" stroke-width="2"/>
  <g stroke="#fb8c00" stroke-width="1.6" fill="#fff">
    <circle cx="206" cy="14" r="6"/><circle cx="483" cy="12" r="6"/><circle cx="765" cy="16" r="6"/>
  </g>
</svg>

<section class="cta-band"></section>
<h2 class="cta-title">Yes, I Want Mara to Show me How</h2>
<a class="btn-outline" href="#">Click here Now!</a>

<footer class="site-footer">
  <span style="left:99px">maravelin.studio</span>
  <span style="left:234px">|</span>
  <span style="left:254px">lumaro media inc</span>
  <a href="#" style="left:758px">About</a>
  <a href="#" style="left:826px">Contact</a>
</footer>

</body>
</html>
```